Psychic / Tarot Reader needs updated Friendly Page

We need a new design for our Friendly page.
Logo is attached and copy of new website that is being launched.
We need something fresh, simple and eye catching

current Friendly: MoonWillowGlow

layout for entire Friendly please

Target Market(s)

18 +

Requirements
Must have
• colours
• easy to use
• services

```html
<!DOCTYPE html>
<html lang="en">
<head>
<meta charset="utf-8">
<title>MoonWillowGlow – Page Layout</title>
<link href="https://fonts.googleapis.com/css2?family=Montserrat:wght@400;700&family=Roboto:wght@400;500;700&display=swap" rel="stylesheet">
<style>
  :root{
    --bar-blue:#3b5998;
    --page-bg:#e9ebee;
    --white:#ffffff;
    --border:#dddfe2;
    --nav-active:#dfe1e6;
    --nav-accent:#4267b2;
    --text-dark:#1d2129;
    --text-mid:#4b4f56;
    --cover-purple:#8e1f8f;
    --cover-deep:#7a1878;
    --glow-violet:#b46be8;
    --brand-purple:#8a2a8c;
    --cta-blue:#4080ff;
    --btn-bg:#f6f7f9;
  }
  *{margin:0;padding:0;box-sizing:border-box}
  html,body{width:1200px;height:384px;overflow:hidden;background:var(--page-bg);font-family:"Roboto",Arial,sans-serif}
  .canvas{position:relative;width:1200px;height:384px}

  .top-bar{position:absolute;left:0;top:0;width:1200px;height:38px;background:var(--bar-blue);border-bottom:1px solid #29487d}
  .network-mark{position:absolute;left:132px;top:6px;width:22px;height:22px;background:var(--white);border-radius:2px}
  .search-box{position:absolute;left:163px;top:7px;width:394px;height:21px;background:var(--white);border-radius:2px;font-size:12px;color:var(--text-dark);line-height:21px;padding-left:9px}
  .search-btn{position:absolute;right:0;top:0;width:41px;height:21px;background:var(--btn-bg);border-left:1px solid var(--border)}
  .search-btn svg{position:absolute;left:14px;top:5px}
  .user-avatar{position:absolute;left:732px;top:8px;width:20px;height:20px;background:#b9a89a;border-radius:1px}
  .user-name,.home-link{position:absolute;top:10px;color:var(--white);font-size:11px;font-weight:700}
  .user-name{left:758px}
  .home-link{left:832px;padding-left:9px;border-left:1px solid #2d4680}
  .bar-icon{position:absolute;top:9px}

  .profile-box{position:absolute;left:133px;top:49px;width:151px;height:149px;background:var(--white);border:1px solid var(--border);border-radius:2px;padding:4px}
  .profile-inner{width:100%;height:100%;border:1px solid #ccd0d5;display:flex;align-items:center;justify-content:center}
  .brand-name{font-family:"Montserrat",sans-serif;font-weight:700;font-size:14px;color:var(--brand-purple)}

  .side-nav{position:absolute;left:132px;top:225px;width:155px;list-style:none}
  .side-nav li{height:28px;line-height:28px;padding-left:9px;font-size:12px;color:var(--text-mid)}
  .side-nav .active{background:var(--nav-active);border-left:3px solid var(--nav-accent);padding-left:7px;color:var(--text-dark);font-weight:500;font-size:13px}

  .cover{position:absolute;left:295px;top:38px;width:738px;height:280px;background:radial-gradient(circle at 30% 40%,#a02ea0 0%,var(--cover-purple) 45%,var(--cover-deep) 100%);overflow:hidden}
  .cover-copy{position:absolute;left:38px;top:82px;width:358px;text-align:center;color:var(--white);font-family:"Montserrat",sans-serif}
  .cover-title{font-size:20px;font-weight:700;letter-spacing:.2px;margin-bottom:8px}
  .cover-text{font-size:11px;line-height:16.6px}
  .meditation-art{position:absolute;left:408px;top:14px;width:252px;height:252px;border-radius:50%;background:radial-gradient(circle,#c58af0 0%,#9c4cd6 45%,#7d2fb8 70%,rgba(142,31,143,0) 72%);box-shadow:0 0 18px 4px rgba(200,140,255,.55)}

  .action-bar{position:absolute;left:295px;top:318px;width:736px;height:45px;background:var(--white);border:1px solid var(--border);border-top:none}
  .btn-group{position:absolute;left:12px;top:10px;display:flex;height:25px;border:1px solid #ced0d4;border-radius:2px;background:var(--btn-bg)}
  .btn{display:flex;align-items:center;gap:4px;padding:0 8px;font-size:11px;font-weight:700;color:var(--text-mid);border-right:1px solid #ced0d4}
  .btn:last-child{border-right:none}
  .btn.liked{width:76px}.btn.message{width:83px}.btn.more{width:75px}
  .contact-btn{position:absolute;left:460px;top:10px;width:265px;height:25px;background:var(--cta-blue);color:var(--white);border-radius:2px;font-size:13px;line-height:25px;text-align:center}
</style>
</head>
<body>
<div class="canvas">
  <header class="top-bar">
    <div class="network-mark"></div>
    <div class="search-box">DesignStash.com
      <span class="search-btn"><svg width="11" height="11" viewBox="0 0 11 11"><circle cx="4.5" cy="4.5" r="3.5" fill="none" stroke="#606770" stroke-width="1.4"/><line x1="7" y1="7" x2="10" y2="10" stroke="#606770" stroke-width="1.4"/></svg></span>
    </div>
    <div class="user-avatar"></div>
    <span class="user-name">Sam Carter</span>
    <span class="home-link">Home</span>
    <svg class="bar-icon" style="left:891px" width="18" height="18" viewBox="0 0 18 18"><circle cx="6" cy="5" r="3" fill="#fff"/><path d="M1 16c0-4 2-6 5-6s5 2 5 6z" fill="#fff"/><circle cx="12" cy="5" r="2.5" fill="#fff"/><path d="M12 9c3 0 5 2 5 6h-4z" fill="#fff"/></svg>
    <svg class="bar-icon" style="left:921px" width="18" height="18" viewBox="0 0 18 18"><rect x="4" y="1" width="13" height="9" rx="1.5" fill="#fff"/><path d="M1 6h11v8H5l-3 3v-3H1z" fill="#fff" stroke="#3b5998" stroke-width="1"/></svg>
    <svg class="bar-icon" style="left:950px" width="18" height="18" viewBox="0 0 18 18"><circle cx="9" cy="9" r="8" fill="#fff"/><path d="M5 4c2 1 3 3 1 5s0 4 2 6M12 3c-1 2 1 3 3 4" stroke="#3b5998" stroke-width="1.5" fill="none"/></svg>
    <svg class="bar-icon" style="left:1000px;top:12px" width="26" height="12" viewBox="0 0 26 12"><rect x="1" y="4" width="9" height="7" fill="#1d2d50"/><path d="M3 4V2.5a2.5 2.5 0 015 0V4" stroke="#1d2d50" stroke-width="1.4" fill="none"/><path d="M17 4h8l-4 5z" fill="#1d2d50"/></svg>
  </header>

  <div class="profile-box"><div class="profile-inner"><span class="brand-name">MoonWillowGlow</span></div></div>

  <ul class="side-nav">
    <li class="active">Home</li>
    <li>Photos</li>
    <li>Likes</li>
  </ul>

  <section class="cover">
    <div class="cover-copy">
      <h1 class="cover-title">WELCOME TO MOONWILLOWGLOW</h1>
      <p class="cover-text">Elara has completed various training courses to give her an indepth knowledge of Tarot and Reiki whilst applying her intution to give her clients indepth readings. She aims to offer clients guidance and support in any area of their life through the use of these methods.</p>
    </div>
    <div class="meditation-art" role="img" aria-label="Glowing illustration of a meditating figure with chakra symbols inside a violet ring"></div>
  </section>

  <div class="action-bar">
    <div class="btn-group">
      <span class="btn liked"><svg width="11" height="11" viewBox="0 0 11 11"><path d="M1 5h2v6H1zM4 5l2-4c1 0 1.5.5 1.3 2L7 4.5h3l-1 6H4z" fill="#4267b2"/></svg>Liked <svg width="7" height="4" viewBox="0 0 7 4"><path d="M0 0h7L3.5 4z" fill="#606770"/></svg></span>
      <span class="btn message"><svg width="11" height="11" viewBox="0 0 11 11"><circle cx="5.5" cy="5" r="5" fill="#90949c"/></svg>Message</span>
      <span class="btn more"><svg width="12" height="3" viewBox="0 0 12 3"><circle cx="1.5" cy="1.5" r="1.3" fill="#90949c"/><circle cx="6" cy="1.5" r="1.3" fill="#90949c"/><circle cx="10.5" cy="1.5" r="1.3" fill="#90949c"/></svg>More <svg width="7" height="4" viewBox="0 0 7 4"><path d="M0 0h7L3.5 4z" fill="#606770"/></svg></span>
    </div>
    <div class="contact-btn">Contact Us</div>
  </div>
</div>
</body>
</html>
```